Real Estate Managemene Company Needs Business Card Design

We have a logo design and just need business cards made now for our business. Please use PDF logo # 3.

Card with Information to be attached shortly.

The card is used for a real estate management company. We will need to add four other employees and their cards.

Industry/Entity Type

Real Estate

Contact Information for Business Card

Tariq Hamdan
President
3187 Thornwick Avenue
Suite C
Glendale Heights, IL 60152
Phone 630.417.2286
Fax 630.417.2287
Cell 630.473.8062
vantorp@mailbreeze.net

Once design is approved we will have four other employees
Omar Hamdan
Operations Manager

Nadia Hamdan
Administrative Manager

Faz Hamdan
Principal

We would need to take out the cell # 630.473.8062 out for the remaining three cards.

Requirements
Must have
• Please use logo attached

```html
<!DOCTYPE html>
<html lang="en">
<head>
<meta charset="utf-8">
<title>Larkmoor Property Group – Business Card</title>
<link href="https://fonts.googleapis.com/css2?family=Oswald:wght@300;400&family=Montserrat:wght@800&display=swap" rel="stylesheet">
<style>
  :root {
    --bg: #1d1d1d;
    --paper: #f2f2f2;
    --red: #c8202f;
    --ink: #2a2a2a;
    --white: #ffffff;
  }
  html, body {
    margin: 0;
    padding: 0;
    width: 1200px;
    height: 800px;
    overflow: hidden;
    background: var(--bg);
  }
  .canvas {
    width: 1200px;
    height: 800px;
    display: flex;
    align-items: center;
    justify-content: center;
  }
  .card {
    position: relative;
    width: 1050px;
    height: 600px;
    border-radius: 34px;
    overflow: hidden;
    background: var(--paper);
    font-family: "Oswald", "Arial Narrow", sans-serif;
  }
  .card__band {
    position: absolute;
    left: 0;
    right: 0;
    top: 250px;
    bottom: 0;
    background: var(--red);
  }
  .brand {
    position: absolute;
    top: 160px;
    left: 0;
    right: 0;
    display: flex;
    align-items: center;
    justify-content: center;
    gap: 16px;
  }
  .brand__mark {
    width: 42px;
    height: 42px;
    background: var(--red);
  }
  .brand__name {
    font-family: "Montserrat", sans-serif;
    font-weight: 800;
    font-size: 36px;
    letter-spacing: 1px;
    color: var(--red);
    text-transform: uppercase;
  }
  .holder {
    position: absolute;
    top: 262px;
    left: 0;
    right: 0;
    margin: 0;
    text-align: center;
    color: var(--white);
    white-space: nowrap;
    font-weight: 300;
  }
  .holder__name {
    font-size: 92px;
    line-height: 1;
    text-transform: uppercase;
  }
  .holder__title {
    font-size: 36px;
    color: var(--ink);
    text-transform: uppercase;
    margin-left: 8px;
  }
  .address {
    position: absolute;
    top: 392px;
    left: 0;
    right: 0;
    margin: 0;
    text-align: center;
    font-weight: 300;
    font-size: 31px;
    color: var(--ink);
    white-space: nowrap;
  }
  .contacts {
    position: absolute;
    top: 478px;
    left: 30px;
    right: 30px;
    margin: 0;
    padding: 0;
    list-style: none;
    display: flex;
    justify-content: space-between;
    align-items: center;
  }
  .contact {
    display: flex;
    align-items: center;
    gap: 10px;
    color: var(--white);
    font-weight: 300;
    font-size: 27px;
    white-space: nowrap;
  }
  .contact__icon {
    width: 44px;
    height: 44px;
    border-radius: 50%;
    background: var(--white);
    display: flex;
    align-items: center;
    justify-content: center;
    flex: none;
  }
  .contact__icon svg {
    width: 24px;
    height: 24px;
    fill: var(--red);
  }
</style>
</head>
<body>
<main class="canvas">
  <article class="card">
    <div class="card__band"></div>

    <header class="brand">
      <span class="brand__mark"></span>
      <span class="brand__name">Larkmoor Property Group</span>
    </header>

    <h1 class="holder">
      <span class="holder__name">Tariq Hamdan</span><span class="holder__title">President</span>
    </h1>

    <p class="address">3187 Thornwick Avenue, Suite C, Wrenfield Hollow, OH 45871</p>

    <ul class="contacts">
      <li class="contact">
        <span class="contact__icon">
          <svg viewBox="0 0 24 24" aria-hidden="true"><path d="M6.6 10.8a15.1 15.1 0 0 0 6.6 6.6l2.2-2.2a1 1 0 0 1 1-.25 11.4 11.4 0 0 0 3.6.57 1 1 0 0 1 1 1V20a1 1 0 0 1-1 1A17 17 0 0 1 3 4a1 1 0 0 1 1-1h3.5a1 1 0 0 1 1 1c0 1.25.2 2.45.57 3.57a1 1 0 0 1-.25 1z"/></svg>
        </span>
        555.417.2286
      </li>
      <li class="contact">
        <span class="contact__icon">
          <svg viewBox="0 0 24 24" aria-hidden="true"><path d="M7 2h10v5H7zM4 8h16a2 2 0 0 1 2 2v8h-4v4H6v-4H2v-8a2 2 0 0 1 2-2zm4 8v4h8v-4z"/></svg>
        </span>
        555.417.2287
      </li>
      <li class="contact">
        <span class="contact__icon">
          <svg viewBox="0 0 24 24" aria-hidden="true"><path d="M8 1h8a2 2 0 0 1 2 2v18a2 2 0 0 1-2 2H8a2 2 0 0 1-2-2V3a2 2 0 0 1 2-2zm0 3v14h8V4zm4 15.5a1.2 1.2 0 1 0 0 2.4 1.2 1.2 0 0 0 0-2.4z"/></svg>
        </span>
        Cell 555.473.8062
      </li>
      <li class="contact">
        <span class="contact__icon">
          <svg viewBox="0 0 24 24" aria-hidden="true"><path d="M2 5h20v14H2zm2 2v.5l8 5 8-5V7zm0 2.8V17h16V9.8l-8 5z"/></svg>
        </span>
        vantorp@mailbreeze.net
      </li>
    </ul>
  </article>
</main>
</body>
</html>
```